Real Estate Flyer (Brenton Property)

We need a color CMYK high resolution, print quality horizontal real estate property flyer designed in the sizes of 10" wide and 6.7425" tall and another one in 11" wide and 8.5" tall.
Ad should be professionally looking to U.S. standards. It should be sleek, modern yet classy.
We uploaded in Briefs logo files, agent photo, 2 photos of the property (Must use both) and a sample of a flyer for Vayle Morrow Luxury Residence. We like how the overlay atop the first photo in the Vayle Morrow flyer with the company logo in the overlay. We'd like to incorporate that with our logo, the background color of the overlay should match that of our logo. DON'T CHANGE LOGO COLORS. Only use two colors in ad (exact logo blue color and white). The text in the overlay must be "FOR SALE - Potential Income Producing Commercial Office Building". Other details that should be prominent underneath are "42 Brenton Dr., Schaumburg, IL 60174 - Asking Price: $650,000".
Add "Residential & Commercial" under our company logo in italic font.
Add in flyer: "Located seconds away from the Kettering Rd. & Palden Rd. Intersection"
Add in flyer:
- Completely vacant
- 10,000 sq. ft. building
- 55 Car Parking
- 1.38 acre lot
- Over 20 offices and 5 bathrooms.
- Lease out individual office spaces for great monthly cash flow
Put agent's photo and following details professionally displayed:
Dev Marlo
Managing Broker
847-555-0148
dev.marlo@qtnhomes-example.com
Add from Briefs fair housing logo and PLX logo near agent's information. Logos should be small but yet visible to understand text.
Add at bottom of the ad with separation near agent details:
Looking to Buy or Sell?
I’m your one-stop, full service licensed real estate broker.
I deal with all types of real estate properties: Homes, Condos, Townhomes, Multi-Unit Apartment Buildings and Commercial Spaces.
Let My Experience Guide You Through Every Step of the Process!
Fine print:
©2018 QTN Homes, Inc. All Rights Reserved.

```html
<!DOCTYPE html>
<html lang="en">
<head>
<meta charset="utf-8">
<title>Brenton Property – For Sale Flyer</title>
<link rel="stylesheet" href="https://fonts.googleapis.com/css2?family=Lato:ital,wght@0,400;0,700;0,900;1,400&display=swap">
<style>
  :root {
    --brand-blue: #1a4fa6;
    --ink-blue: #1b4c9c;
    --white: #ffffff;
    --paper: #e7e9ee;
    --paper-light: #f1f2f5;
    --ink: #1c1c1c;
  }
  * { box-sizing: border-box; margin: 0; padding: 0; }
  html, body { width: 1200px; height: 840px; overflow: hidden; }
  body { font-family: "Lato", sans-serif; background: var(--white); }

  .flyer {
    position: relative;
    width: 1200px;
    height: 840px;
    overflow: hidden;
    background: linear-gradient(160deg, var(--paper-light), var(--paper) 60%, #dfe3ea);
  }

  .header-art { position: absolute; left: 0; top: 0; width: 1200px; height: 340px; }

  .brand {
    position: absolute; left: 480px; top: 0; width: 238px; height: 205px;
    display: flex; flex-direction: column; align-items: center; justify-content: center;
    color: var(--white); gap: 8px;
  }
  .brand-name { display: flex; align-items: center; gap: 10px; font-weight: 900; font-size: 38px; letter-spacing: 1px; }
  .brand-mark { width: 22px; height: 22px; background: var(--white); }
  .brand-tagline { font-size: 14px; font-style: italic; }

  .headline {
    position: absolute; left: 0; width: 1200px; top: 222px; text-align: center;
    color: var(--brand-blue); font-weight: 900; font-size: 50px; letter-spacing: 0.5px;
  }
  .subhead {
    position: absolute; left: 0; width: 1200px; top: 284px; text-align: center;
    color: var(--ink); font-size: 25px;
  }

  .badge { position: absolute; width: 260px; height: 260px; }
  .badge svg { position: absolute; inset: 0; }
  .badge-text {
    position: absolute; inset: 0; display: flex; flex-direction: column;
    align-items: center; justify-content: center; text-align: center;
    color: var(--white); font-weight: 700; text-transform: uppercase; line-height: 1.15;
  }
  .badge-address { left: 12px; top: 215px; }
  .badge-address .badge-text { transform: rotate(-15deg); font-size: 19px; }
  .badge-address .price { font-size: 36px; font-weight: 900; margin-top: 4px; }
  .badge-location { left: 932px; top: 215px; }
  .badge-location .badge-text { transform: rotate(15deg); font-size: 20px; }

  .features {
    position: absolute; left: 0; width: 1200px; top: 343px; list-style: none;
    text-align: center; color: var(--ink-blue); font-weight: 700; font-size: 34px;
    text-transform: uppercase; line-height: 46.5px;
  }
  .features .wrap { line-height: 36px; margin-top: 6px; }

  .agent-photo {
    position: absolute; left: 0; top: 668px; width: 135px; height: 172px;
    background: linear-gradient(180deg, #f4f4f4, #d9dadd 70%, #2a2d35);
    border-top: 6px solid var(--brand-blue); border-right: 6px solid var(--brand-blue);
    border-top-right-radius: 8px;
  }
  .agent-info { position: absolute; left: 160px; top: 710px; color: var(--ink); font-size: 20px; line-height: 29px; }
  .agent-name { color: var(--brand-blue); font-weight: 900; font-size: 34px; line-height: 36px; text-transform: uppercase; }

  .pitch {
    position: absolute; left: 594px; top: 685px; width: 571px; height: 155px;
    background: var(--brand-blue); border-radius: 14px 14px 0 0;
    color: var(--white); text-align: center; font-size: 16px; line-height: 20px;
    padding: 12px 18px 0;
  }
  .pitch p { margin-bottom: 8px; }
</style>
</head>
<body>
<main class="flyer">
  <svg class="header-art" viewBox="0 0 1200 340" aria-hidden="false">
    <defs>
      <linearGradient id="property-tones" x1="0" y1="0" x2="0" y2="1">
        <stop offset="0" stop-color="#8fb2d8"/>
        <stop offset="0.45" stop-color="#e9dccb"/>
        <stop offset="0.7" stop-color="#b49b7e"/>
        <stop offset="1" stop-color="#4d5248"/>
      </linearGradient>
    </defs>
    <rect x="0" y="0" width="480" height="330" fill="url(#property-tones)" role="img" aria-label="Photo of the office building and parking lot, front view"/>
    <rect x="718" y="0" width="482" height="330" fill="url(#property-tones)" role="img" aria-label="Photo of the office building and parking lot, side view"/>
    <rect x="480" y="0" width="238" height="212" fill="var(--brand-blue)"/>
    <polygon points="0,320 482,214 716,214 1200,320 1200,329 0,329" fill="var(--white)"/>
    <polyline points="0,316 484,210 714,210 1200,316" fill="none" stroke="var(--brand-blue)" stroke-width="9"/>
    <line x1="0" y1="331" x2="1200" y2="331" stroke="var(--brand-blue)" stroke-width="4"/>
  </svg>

  <div class="brand">
    <div class="brand-name"><span class="brand-mark"></span>QTN HOMES</div>
    <div class="brand-tagline">Residential &amp; Commercial</div>
  </div>

  <h1 class="headline">FOR SALE</h1>
  <p class="subhead">Potential Income Producing Commercial Office Building</p>

  <div class="badge badge-address">
    <svg viewBox="0 0 260 260"><circle cx="130" cy="130" r="116" fill="var(--brand-blue)" stroke="var(--brand-blue)" stroke-width="9" stroke-linecap="round" stroke-dasharray="0 11"/></svg>
    <div class="badge-text">
      <span>42 Brenton</span>
      <span>Dr., Schaumburg,</span>
      <span>IL 60174</span>
      <span>Asking Price:</span>
      <span class="price">$650,000</span>
    </div>
  </div>

  <div class="badge badge-location">
    <svg viewBox="0 0 260 260"><circle cx="130" cy="130" r="116" fill="var(--brand-blue)" stroke="var(--brand-blue)" stroke-width="9" stroke-linecap="round" stroke-dasharray="0 11"/></svg>
    <div class="badge-text">
      <span>Located</span>
      <span>seconds away</span>
      <span>from the Kettering</span>
      <span>Rd. &amp; Palden</span>
      <span>Rd. intersection</span>
    </div>
  </div>

  <ul class="features">
    <li>Completely vacant</li>
    <li>10,000 sq. ft. building</li>
    <li>55 car parking</li>
    <li>1.38 acre lot</li>
    <li>Over 20 offices and 5 bathrooms.</li>
    <li class="wrap">Lease out individual office spaces<br>for great monthly cash flow</li>
  </ul>

  <div class="agent-photo" role="img" aria-label="Portrait photo of the managing broker"></div>
  <div class="agent-info">
    <div class="agent-name">Dev Marlo</div>
    <div>Managing Broker</div>
    <div>847-555-0148</div>
    <div>dev.marlo@qtnhomes-example.com</div>
  </div>

  <section class="pitch">
    <p>Looking to Buy or Sell?</p>
    <p>I’m your one-stop, full service licensed real estate broker.</p>
    <p>I deal with all types of real estate properties: Homes, Condos, Townhomes, Multi-Unit Apartment Buildings and Commercial Spaces.</p>
    <p>Let My Experience Guide You Through Every Step of the Process!</p>
  </section>
</main>
</body>
</html>
```